Yard sign for Chimney Buisness

I am looking for a 18 Tall x 24" wide yard sign design incorporating our logo/name. We want the signs to stand out and be readable from a distance. only want our logo/business name and website on the sign . www.tallowmerevt.com

Target Market(s)

homeowners

Requirements
Must have
• logo/buisness name
• website
• must be visable at a distance and readable

```html
<!DOCTYPE html>
<html lang="en">
<head>
<meta charset="utf-8">
<title>Tallowmere Chimney – Yard Sign Set</title>
<link rel="stylesheet" href="https://fonts.googleapis.com/css2?family=Cinzel:wght@500&family=Montserrat:wght@600&family=Open+Sans:wght@700&display=swap">
<style>
  :root {
    --canvas: #ebeceb;
    --red: #990000;
    --charcoal: #353535;
    --white: #ffffff;
  }
  html, body {
    margin: 0;
    width: 1200px;
    height: 1200px;
    overflow: hidden;
    background: var(--canvas);
  }
  .sign-grid {
    position: absolute;
    left: 86px;
    top: 212px;
    display: grid;
    grid-template-columns: 503px 503px;
    grid-template-rows: 376px 376px;
    gap: 23px 22px;
  }
  .sign {
    width: 503px;
    height: 376px;
    border-radius: 7px;
    overflow: hidden;
    display: block;
  }
  .brand-name { font-family: "Cinzel", serif; font-weight: 500; }
  .headline { font-family: "Montserrat", sans-serif; font-weight: 600; }
  .website { font-family: "Open Sans", sans-serif; font-weight: 700; }
</style>
</head>
<body>
<main class="sign-grid">

  <!-- Sign 1: white top, red base -->
  <svg class="sign sign--light" viewBox="0 0 416 311" aria-label="Tallowmere Chimney yard sign, light version">
    <rect width="416" height="311" fill="var(--white)"/>
    <rect class="brand-square" x="159" y="42" width="98" height="98" fill="none" stroke="var(--charcoal)" stroke-width="9"/>
    <text class="brand-name" x="208" y="184" text-anchor="middle" font-size="22" fill="var(--charcoal)">TALLOWMERE CHIMNEY</text>
    <path class="swoosh" d="M0,224 C40,252 140,266 265,234 C150,262 50,262 0,244 Z" fill="var(--charcoal)"/>
    <path class="band" d="M0,252 C130,272 260,232 416,224 L416,311 L0,311 Z" fill="var(--red)"/>
    <text class="website" x="388" y="292" text-anchor="end" font-size="18.5" fill="var(--white)">tallowmerevt.com</text>
  </svg>

  <!-- Sign 2: red top, charcoal base -->
  <svg class="sign sign--red" viewBox="0 0 416 311" aria-label="Tallowmere Chimney yard sign, red version">
    <rect width="416" height="311" fill="var(--red)"/>
    <rect class="brand-square" x="159" y="42" width="98" height="98" fill="none" stroke="var(--white)" stroke-width="9"/>
    <text class="brand-name" x="208" y="184" text-anchor="middle" font-size="22" fill="var(--white)">TALLOWMERE CHIMNEY</text>
    <path class="swoosh" d="M0,224 C40,252 140,266 265,234 C150,262 50,262 0,244 Z" fill="var(--white)"/>
    <path class="band" d="M0,254 C130,272 260,232 416,224 L416,311 L0,311 Z" fill="var(--charcoal)"/>
    <text class="website" x="388" y="292" text-anchor="end" font-size="18.5" fill="var(--white)">tallowmerevt.com</text>
  </svg>

  <!-- Sign 3: large headline -->
  <svg class="sign sign--headline" viewBox="0 0 416 311" aria-label="Tallowmere Chimney yard sign, headline version">
    <rect width="416" height="311" fill="var(--red)"/>
    <rect class="brand-square" x="38" y="30" width="34" height="34" fill="none" stroke="var(--white)" stroke-width="4"/>
    <text class="brand-name" x="82" y="52" font-size="13" fill="var(--white)">TALLOWMERE CHIMNEY</text>
    <text class="headline" x="30" y="134" font-size="48" textLength="354" lengthAdjust="spacingAndGlyphs" fill="var(--white)">TALLOWMERE</text>
    <text class="headline" x="30" y="190" font-size="48" fill="var(--white)">CHIMNEY</text>
    <path class="swoosh" d="M416,224 C370,254 270,262 150,234 C260,262 360,260 416,244 Z" fill="var(--white)"/>
    <path class="band" d="M0,226 C150,222 280,262 416,246 L416,311 L0,311 Z" fill="var(--charcoal)"/>
    <text class="website" x="30" y="290" font-size="18.5" fill="var(--white)">tallowmerevt.com</text>
  </svg>

  <!-- Sign 4: red top, white base -->
  <svg class="sign sign--red-light" viewBox="0 0 416 311" aria-label="Tallowmere Chimney yard sign, red and white version">
    <rect width="416" height="311" fill="var(--white)"/>
    <path class="field" d="M0,0 H416 V230 C300,250 180,240 0,262 Z" fill="var(--red)"/>
    <path class="swoosh" d="M416,226 C330,242 230,244 150,240 C250,250 340,256 416,250 Z" fill="var(--charcoal)"/>
    <rect class="brand-square" x="159" y="42" width="98" height="98" fill="none" stroke="var(--white)" stroke-width="9"/>
    <text class="brand-name" x="208" y="184" text-anchor="middle" font-size="22" fill="var(--white)">TALLOWMERE CHIMNEY</text>
    <text class="website" x="208" y="290" text-anchor="middle" font-size="18.5" fill="var(--red)">tallowmerevt.com</text>
  </svg>

</main>
</body>
</html>
```